meridale partners business card

Architectural firm business card
Updates

Please note:

corporate colour black+yellow are the only elements to be kept.
NO OTHER ELEMENT TO BE REUSED FROM PREVIOUS BUSINESS CARD.
Thank you.

Dear Everyone,

Thank you for your participation. I have upload the KBSO+ logo again for incoporate in the card. in tif and pdf format.

Thank you 

I keep getting request for the logo file. Does everyone has the same problem?

I cannot do much, because the file is upload to the website server. I can't seem to see it either.

The logo file is now working. Please download. I check it myself. Thank you everyone.

Dear All,

Thank you for all the hard work. There are a lot of great work. Due to current commitment with work, I am unable to review them just yet. I will do so next week and advise everyone also. Thank you again. Best regards

Dear All,

Thank you for your participation. There are a lot of good design. Unfortunately, I can only select one. All the best. This is definitely a good crowd to work with. Thank you everyone again.

Best regards

Target Market(s)

Corporate, commercial and institutional projects only

Industry/Entity Type

Business

Requirements
Must have
• elegant simple
double sided with coating
Member of Southland Guild of Draughtsmen (logo only)
corporate colour black and

LOGO FILE UPLOADED
Should not have
• should not be the same as current business card.
upload for reference information only.
font sans serif preferred.

```html
<!DOCTYPE html>
<html lang="en">
<head>
<meta charset="utf-8">
<title>Meridale Partners — Business Card</title>
<link rel="stylesheet" href="https://fonts.googleapis.com/css2?family=PT+Sans+Narrow:wght@400;700&display=swap">
<style>
  :root {
    --orange: #f18a22;
    --ink: #1c1c1c;
    --navy: #2d2a3d;
    --navy-light: #5b5772;
    --paper: #ffffff;
    --stage: #e6e6e6;
    --grey: #4a4a4a;
  }
  * { box-sizing: border-box; margin: 0; padding: 0; }
  html, body { width: 1200px; height: 646px; overflow: hidden; }
  body {
    background: var(--stage);
    font-family: "PT Sans Narrow", "Arial Narrow", sans-serif;
    position: relative;
  }
  .card {
    position: absolute;
    top: 178px;
    width: 520px;
    height: 289px;
    overflow: hidden;
    box-shadow: 0 6px 18px rgba(0,0,0,0.18);
  }

  /* Back side */
  .card-back {
    left: 50px;
    background: radial-gradient(ellipse 60% 70% at 50% 38%, var(--navy-light) 0%, var(--navy) 70%);
  }
  .card-back .streaks { position: absolute; right: 0; top: 0; }
  .back-brand {
    position: absolute; left: 0; right: 0; top: 92px;
    text-align: center; color: var(--paper);
  }
  .brand-mark {
    display: inline-flex; align-items: center; gap: 10px;
    font-weight: 700; font-size: 30px; letter-spacing: 0.5px;
  }
  .brand-square { width: 26px; height: 26px; background: var(--orange); display: inline-block; }
  .back-services {
    margin-top: 10px; color: var(--orange); font-size: 17px; font-weight: 400;
  }
  .back-services .sep { color: var(--paper); margin: 0 6px; }
  .back-web {
    margin-top: 26px; font-size: 19px; color: var(--paper);
  }

  /* Front side */
  .card-front { left: 630px; background: var(--paper); }
  .front-tint {
    position: absolute; right: 0; top: 0; width: 250px; height: 230px;
    background: linear-gradient(120deg, rgba(241,138,34,0) 30%, rgba(241,138,34,0.12) 100%);
  }
  .front-brand { position: absolute; left: 36px; top: 120px; color: var(--ink); }
  .front-brand .brand-mark { font-size: 26px; gap: 8px; }
  .front-brand .brand-square { width: 22px; height: 22px; }
  .front-services {
    margin-top: 6px; margin-left: 74px; color: var(--orange);
    font-size: 16px; line-height: 1.05;
  }
  .person { position: absolute; left: 226px; top: 22px; color: var(--ink); }
  .person-name { font-size: 27px; font-weight: 700; }
  .person-name .postnominals { font-size: 14px; font-weight: 400; margin-left: 4px; }
  .person-credential { font-size: 13px; color: var(--grey); }
  .person-role { font-size: 19px; color: var(--orange); line-height: 1.05; }
  .person-mobile { font-size: 17px; font-weight: 700; }
  .contact-list {
    position: absolute; left: 240px; top: 132px; list-style: none;
    font-size: 14.5px; color: var(--ink); line-height: 1.12;
  }
  .contact-list li { display: flex; align-items: center; gap: 8px; }
  .contact-list svg { width: 13px; height: 13px; flex: none; fill: var(--orange); }
  .contact-list .address { align-items: flex-start; margin-top: 4px; }
  .contact-list .address svg { margin-top: 16px; }
  .base-bands { position: absolute; left: 0; bottom: 0; }
</style>
</head>
<body>

<section class="card card-back" aria-label="Card back">
  <svg class="streaks" width="160" height="150" viewBox="0 0 160 150" aria-hidden="true">
    <path d="M70 0 L86 0 L30 150 L14 150 Z" fill="rgba(255,255,255,0.06)"/>
    <path d="M96 0 L104 0 L50 150 L42 150 Z" fill="rgba(255,255,255,0.08)"/>
    <path d="M118 0 L124 0 L70 150 L64 150 Z" fill="rgba(255,255,255,0.05)"/>
  </svg>
  <div class="back-brand">
    <div class="brand-mark"><span class="brand-square"></span>Meridale Partners</div>
    <div class="back-services">architects<span class="sep">|</span>urban designers<span class="sep">|</span>project managers</div>
    <div class="back-web">www.meridalepartners.com.au</div>
  </div>
</section>

<section class="card card-front" aria-label="Card front">
  <div class="front-tint"></div>

  <div class="front-brand">
    <div class="brand-mark"><span class="brand-square"></span>Meridale Partners</div>
    <div class="front-services">architects<br>urban designers<br>project managers</div>
  </div>

  <div class="person">
    <div class="person-name">Linh Carver<span class="postnominals">kbso, sgpm</span></div>
    <div class="person-credential">Architect (SGD reg. no: 7214)</div>
    <div class="person-role">Director</div>
    <div class="person-mobile">M 0412 770 845</div>
  </div>

  <ul class="contact-list">
    <li><svg viewBox="0 0 16 16"><path d="M3 1 L6 1 L7 5 L5 6.5 C6 9 7.5 10.5 10 11.5 L11.5 9.5 L15 10.5 L15 13.5 C15 14.5 14 15 13 15 C6.5 14.5 1.5 9.5 1 3 C1 2 1.8 1 3 1 Z"/></svg>+612 9148 2207</li>
    <li><svg viewBox="0 0 16 16"><rect x="4" y="1" width="8" height="5"/><rect x="1" y="6" width="14" height="7" rx="1"/><rect x="4" y="11" width="8" height="4" fill="#fff"/></svg>+612 9148 2290</li>
    <li><svg viewBox="0 0 16 16"><rect x="1" y="3" width="14" height="10"/><path d="M1 3 L8 9 L15 3" fill="none" stroke="#fff" stroke-width="1.4"/></svg>studio@meridalepartners.com.au</li>
    <li><svg viewBox="0 0 16 16"><circle cx="8" cy="8" r="7"/><path d="M1 8 H15 M8 1 C4 5 4 11 8 15 M8 1 C12 5 12 11 8 15" fill="none" stroke="#fff" stroke-width="1"/></svg>www.meridalepartners.com.au</li>
    <li class="address"><svg viewBox="0 0 16 16"><path d="M8 1 L15 8 L13 8 L13 15 L9.5 15 L9.5 10.5 L6.5 10.5 L6.5 15 L3 15 L3 8 L1 8 Z"/></svg><span>Alder House<br>18 Quarry Lane, Westmere NSW 2149</span></li>
  </ul>

  <svg class="base-bands" width="520" height="40" viewBox="0 0 520 40" aria-hidden="true">
    <path d="M0 16 L300 16 L300 40 L0 40 Z" fill="var(--orange)"/>
    <path d="M300 0 L520 0 L520 40 L300 40 Z" fill="var(--ink)"/>
  </svg>
</section>

</body>
</html>
```